Automotive Mechanic Website Design

We are working with an auto repair shop in California.
A few websites for inspiration:
https://northbaymotorcraft.com
https://www.portfoliqo.net/gallery/51730486/Velmora-Auto-Services-Repair-SiteKit-Theme
http://www.grindvoltmotors.com
https://www.keelbrant.net
https://www.tvgaragecraft.com
Thank you for taking the time to consider designing a website for us. We are web developers based in Stockton, CA, USA. Most of our projects go through the same process. Understanding this process may help you win a project with us. We custom-code all of our websites in-house. We don’t have any requirements as to what tools you use for your design, but we ask that you follow these guidelines.
IMAGES:
If you use any images or icons in the design, we ask that you have a link to the asset so we can purchase the image/icon. Most of the designs we submit do not have the customer’s images on them unless they have some great images. Be creative; show us the feeling you are trying to portray with your image choices. Use any royalty-free site you choose. We subscribe to Quillo and mainly use their images, but we can purchase images outside of Quillo. PLEASE NOTE: we will not submit designs to clients with watermarks on the images.
FONTS:
We ask that you identify the fonts you’re using in the design. This can be done in a message if you want. We typically use Typora Fonts and Quillo Fonts.
CONTENT:
We're always open to different content and ideas. We often submit designs with stock images so the client can see our vision. We typically take pictures after the website launch to use their images with our vision. Lorem Ipsum is fine for paragraphs, but we ask that you make the Headers with correct English. We want to be able to show the vision and identify the sections of the website.
INSPIRATION:
We typically add a couple of links in the brief of websites we like to help you get started in your design.
REVISIONS:
We do not often ask for revisions of the designs unless we see something in the design that may not appeal to the client. If there are slight changes that we want to make, we do that in the development process.
FEEDBACK:
We rarely give feedback on designs during the design process. We are working on many website projects and do not have the time to provide feedback. We usually respond if your request is well thought out and asks specific questions, but a note asking “feedback, please” usually goes unanswered.

```html
<!DOCTYPE html>
<html lang="en">
<head>
<meta charset="utf-8">
<title>Kestrel Auto Repair</title>
<link rel="stylesheet" href="https://fonts.googleapis.com/css2?family=Poppins:wght@400;500;600;700;800&display=swap">
<style>
:root{
  --red:#e8313c;
  --red-dark:#c91f2a;
  --ink:#141414;
  --text:#555;
  --head-bg:#f6eeee;
  --band:#ebe3e3;
  --stats:#e6dcdc;
  --white:#fff;
  --black:#050505;
}
*{margin:0;padding:0;box-sizing:border-box}
html,body{width:1200px;height:4471px;overflow:hidden}
body{position:relative;font-family:'Poppins',sans-serif;color:var(--ink);background:var(--white)}
.abs{position:absolute}
.btn{position:absolute;background:var(--red);color:var(--white);font-weight:700;font-size:14px;display:flex;align-items:center;justify-content:center;text-decoration:none}
.photo{position:absolute}
.section-title{position:absolute;left:0;width:1200px;text-align:center;font-weight:700;font-size:36px;color:var(--ink)}

/* header */
.site-header{position:absolute;left:0;top:0;width:1200px;height:84px;background:var(--head-bg)}
.brand{position:absolute;left:105px;top:24px;font-weight:800;font-size:26px;color:var(--red);letter-spacing:.5px}
.nav{position:absolute;top:32px;font-size:16px;font-weight:500;color:var(--ink)}
.quote-btn{left:952px;top:20px;width:133px;height:48px;font-size:15px}

/* hero */
.hero{position:absolute;left:0;top:84px;width:1200px;height:540px;overflow:hidden}
.hero-photo{left:0;top:0;width:1200px;height:540px;background:linear-gradient(90deg,#2b2d31 0%,#4a4d52 45%,#6d6f72 70%,#3e4145 100%)}
.hero h1{position:absolute;left:110px;top:100px;color:var(--white);font-weight:800;font-size:50px;line-height:52px;text-transform:uppercase}
.hero-btn{left:108px;top:288px;width:132px;height:49px}
.hero-curve{position:absolute;left:0;top:470px}

/* who */
.who h2{position:absolute;left:110px;top:666px;font-size:34px;font-weight:700}
.who p{position:absolute;left:110px;top:722px;width:455px;font-size:14px;line-height:25.6px;color:var(--text)}
.who-btn{left:108px;top:1004px;width:132px;height:48px}
.who-block{left:757px;top:670px;width:443px;height:346px;background:var(--red)}
.who-photo{left:600px;top:710px;width:335px;height:352px;background:linear-gradient(160deg,#3b5a7a,#6a4a34 60%,#222)}

/* offer */
.offer-band{position:absolute;left:0;top:1160px;width:1200px;height:570px;background:var(--band)}
.offer-card{position:absolute;top:1297px;width:220px;height:355px;background:var(--white);box-shadow:0 2px 10px rgba(0,0,0,.08);text-align:center}
.offer-icon{position:absolute;left:80px;top:48px;width:60px;height:60px;background:var(--red);border-radius:8px}
.offer-card h3{position:absolute;left:0;top:128px;width:220px;font-size:24px;font-weight:500;line-height:38px}
.offer-card p{position:absolute;left:0;top:215px;width:220px;font-size:14px;line-height:25px;color:var(--ink)}
.offer-card .btn{left:43px;top:283px;width:134px;height:50px}
.arrow{position:absolute}

/* why */
.why-square{left:108px;top:1786px;width:100px;height:114px;background:var(--red)}
.why-photo{left:135px;top:1807px;width:393px;height:305px;background:linear-gradient(135deg,#4d5560,#27303c 55%,#8a8f96)}
.why-badge{position:absolute;left:435px;top:2000px;width:130px;height:130px;border-radius:50%;background:var(--red);color:var(--white);font-weight:800;font-size:28px;line-height:26px;text-align:center;display:flex;align-items:center;justify-content:center}
.why h2{position:absolute;left:596px;top:1798px;font-size:36px;font-weight:700}
.why p{position:absolute;left:598px;top:1862px;width:490px;font-size:14px;line-height:26px;color:var(--text)}
.tick{position:absolute;left:598px;font-size:14px;color:var(--text);display:flex;align-items:center;gap:8px}
.why-btn{left:598px;top:2056px;width:134px;height:50px}

/* team */
.team-photo{position:absolute;top:2312px;width:269px;height:313px;background:linear-gradient(170deg,#6f7a88,#25324a 60%,#9d2230)}
.corner{position:absolute;border-color:var(--red);border-style:solid}
.team-overlay{position:absolute;left:462px;top:2312px;width:269px;height:313px;background:rgba(232,49,60,.82);color:var(--white);text-align:center}
.team-overlay .name{position:absolute;top:192px;width:100%;font-size:24px;font-weight:700}
.team-overlay .role{position:absolute;top:228px;width:100%;font-size:14px}
.socials{position:absolute;top:258px;left:0;width:100%;display:flex;justify-content:center;gap:12px}
.socials span{width:24px;height:24px;border:1.5px solid var(--white);border-radius:50%}

/* stats */
.stats{position:absolute;left:0;top:2733px;width:1200px;height:247px;background:var(--stats)}
.stat{position:absolute;top:80px;width:240px;margin-left:-120px;text-align:center}
.stat b{display:block;font-size:44px;font-weight:700;line-height:50px}
.stat span{display:block;font-size:24px;font-weight:500;margin-top:10px}

/* blogs */
.blog-card{position:absolute;top:3148px;width:293px;height:404px;background:var(--white);box-shadow:0 2px 12px rgba(0,0,0,.12)}
.blog-photo{position:absolute;left:11px;top:10px;width:271px;height:204px}
.blog-card .date{position:absolute;left:13px;top:230px;font-size:14px}
.blog-card h3{position:absolute;left:13px;top:255px;width:270px;font-size:23px;font-weight:600;line-height:26px}
.blog-card .btn{left:67px;top:330px;width:138px;height:48px}

/* testimonials */
.testi-band{position:absolute;left:0;top:3838px;width:1200px;height:277px;background:var(--red)}
.testi-card{position:absolute;top:3698px;width:380px;height:372px;background:var(--white);box-shadow:0 2px 10px rgba(0,0,0,.08)}
.testi-card .qm{position:absolute;left:20px;top:26px;font-size:80px;font-weight:800;color:var(--red);line-height:80px}
.testi-card p{position:absolute;left:20px;top:90px;width:290px;font-size:14px;line-height:25.6px;color:var(--text)}
.avatar{position:absolute;left:20px;top:280px;width:68px;height:68px;border-radius:50%;background:linear-gradient(#c9d3dc,#6e7c8c)}
.testi-card .who-name{position:absolute;left:96px;top:284px;font-size:17px}
.testi-card .who-role{position:absolute;left:96px;top:312px;font-size:14px;color:var(--text)}

/* footer */
.footer{position:absolute;left:0;top:4115px;width:1200px;height:356px;background:var(--black);color:var(--white)}
.foot-brand{position:absolute;left:0;top:60px;width:1200px;text-align:center;font-size:26px;font-weight:800}
.foot-h{position:absolute;font-size:16px;font-weight:600}
.foot-t{position:absolute;font-size:14px;line-height:25px}
.foot-btn{left:823px;top:213px;width:137px;height:47px}
.foot-line{position:absolute;left:108px;top:324px;width:976px;height:1px;background:#444}
.copyright{position:absolute;left:0;top:333px;width:1200px;text-align:center;font-size:12px}
</style>
</head>
<body>

<header class="site-header">
  <div class="brand">Kestrel Auto Repair</div>
  <span class="nav" style="left:588px">Home</span>
  <span class="nav" style="left:671px">Blogs</span>
  <span class="nav" style="left:745px">Shop</span>
  <span class="nav" style="left:817px">Contact Us</span>
  <a class="btn quote-btn">Get A Quote</a>
</header>

<section class="hero">
  <div class="photo hero-photo" role="img" aria-label="Smiling mechanic in cap with arms crossed in a repair workshop"></div>
  <h1>Welcome to<br>Kestrel<br>Auto Repair</h1>
  <a class="btn hero-btn">Read More</a>
  <svg class="hero-curve" width="1200" height="70" viewBox="0 0 1200 70">
    <path d="M0 70 L0 62 Q600 -30 1200 46 L1200 70 Z" fill="#e8313c"/>
    <path d="M0 70 Q600 -15 1200 62 L1200 70 Z" fill="#fff"/>
  </svg>
</section>

<section class="who">
  <h2>Who We are</h2>
  <p>Lorem Ipsum is simply dummy text of the printing and typesetting industry. Lorem Ipsum has been the industry's standard dummy text ever since the 1500s, when an unknown printer took a galley of type and scrambled it to make a type specimen book. It has survived not only five centuries creating custom software applications that help our clients increase productivity, streamline operations, and improve customer engagement. With a focus on enterprise-level clients, we take a consultative approach to understand our client's unique needs and deliver solutions that are tailored to their specific</p>
  <a class="btn who-btn">Read More</a>
  <div class="abs who-block"></div>
  <div class="photo who-photo" role="img" aria-label="Bearded mechanic in overalls holding a tyre"></div>
</section>

<section class="offer">
  <div class="offer-band"></div>
  <h2 class="section-title" style="top:1212px">What We Offer</h2>
  <svg class="arrow" style="left:40px;top:1450px" width="16" height="26" viewBox="0 0 16 26"><path d="M13 2 L3 13 L13 24" stroke="#141414" stroke-width="2.5" fill="none"/></svg>
  <svg class="arrow" style="left:1122px;top:1450px" width="16" height="26" viewBox="0 0 16 26"><path d="M3 2 L13 13 L3 24" stroke="#141414" stroke-width="2.5" fill="none"/></svg>
  <div class="offer-card" style="left:108px"><div class="offer-icon" role="img" aria-label="Oil change icon"></div><h3>Lorem Ipsum<br>simply</h3><p>Lorem Ipsum is simply<br>dummy text of the</p><a class="btn">Read More</a></div>
  <div class="offer-card" style="left:361px"><div class="offer-icon" role="img" aria-label="Engine service icon"></div><h3>Lorem Ipsum<br>simply</h3><p>Lorem Ipsum is simply<br>dummy text of the</p><a class="btn">Read More</a></div>
  <div class="offer-card" style="left:613px"><div class="offer-icon" role="img" aria-label="Battery service icon"></div><h3>Lorem Ipsum<br>simply</h3><p>Lorem Ipsum is simply<br>dummy text of the</p><a class="btn">Read More</a></div>
  <div class="offer-card" style="left:864px"><div class="offer-icon" role="img" aria-label="Car lift repair icon"></div><h3>Lorem Ipsum<br>simply</h3><p>Lorem Ipsum is simply<br>dummy text of the</p><a class="btn">Read More</a></div>
</section>

<section class="why">
  <div class="abs why-square"></div>
  <div class="photo why-photo" role="img" aria-label="Mechanic with wrench working under an open car bonnet"></div>
  <div class="why-badge">Best<br>Service</div>
  <h2>Why Choose Us</h2>
  <p>Lorem Ipsum is simply dummy text of the printing and typesetting industry. Lorem Ipsum has been. the industry's standard dummy text ever since the 1500s, when an unknown printer took a galley of</p>
  <div class="tick" style="top:1952px"><svg width="16" height="14" viewBox="0 0 16 14"><path d="M1 7 L6 12 L15 1" stroke="#e8313c" stroke-width="2.5" fill="none"/></svg>Lorem Ipsum is simply dummy text of the printing</div>
  <div class="tick" style="top:1978px"><svg width="16" height="14" viewBox="0 0 16 14"><path d="M1 7 L6 12 L15 1" stroke="#e8313c" stroke-width="2.5" fill="none"/></svg>Lorem Ipsum is simply dummy text of the printing</div>
  <div class="tick" style="top:2005px"><svg width="16" height="14" viewBox="0 0 16 14"><path d="M1 7 L6 12 L15 1" stroke="#e8313c" stroke-width="2.5" fill="none"/></svg>Lorem Ipsum is simply dummy text of the printing</div>
  <a class="btn why-btn">Read More</a>
</section>

<section class="team">
  <h2 class="section-title" style="top:2207px">Our Team</h2>
  <div class="corner" style="left:95px;top:2298px;width:75px;height:60px;border-width:14px 0 0 14px"></div>
  <div class="corner" style="left:318px;top:2580px;width:72px;height:60px;border-width:0 14px 14px 0"></div>
  <div class="corner" style="left:449px;top:2298px;width:75px;height:60px;border-width:14px 0 0 14px"></div>
  <div class="corner" style="left:672px;top:2580px;width:72px;height:60px;border-width:0 14px 14px 0"></div>
  <div class="corner" style="left:804px;top:2298px;width:75px;height:60px;border-width:14px 0 0 14px"></div>
  <div class="corner" style="left:1027px;top:2580px;width:72px;height:60px;border-width:0 14px 14px 0"></div>
  <div class="team-photo" style="left:108px" role="img" aria-label="Female mechanic in red and navy uniform with team behind"></div>
  <div class="team-photo" style="left:462px" role="img" aria-label="Senior mechanic in workshop"></div>
  <div class="team-overlay">
    <div class="name">Marisol</div>
    <div class="role">Senior Mechanic</div>
    <div class="socials"><span></span><span></span><span></span></div>
  </div>
  <div class="team-photo" style="left:817px" role="img" aria-label="Male mechanic holding a wrench in workshop"></div>
</section>

<section class="stats">
  <div class="stat" style="left:208px"><b>1000+</b><span>Happy&nbsp; Clients</span></div>
  <div class="stat" style="left:478px"><b>20+</b><span>Years Of service</span></div>
  <div class="stat" style="left:752px"><b>1234+</b><span>Vehicles Repair</span></div>
  <div class="stat" style="left:976px"><b>65</b><span>Awards</span></div>
</section>

<section class="blogs">
  <h2 class="section-title" style="top:3050px">Our Blogs</h2>
  <svg class="arrow" style="left:46px;top:3260px" width="16" height="26" viewBox="0 0 16 26"><path d="M13 2 L3 13 L13 24" stroke="#141414" stroke-width="2.5" fill="none"/></svg>
  <svg class="arrow" style="left:1118px;top:3260px" width="16" height="26" viewBox="0 0 16 26"><path d="M3 2 L13 13 L3 24" stroke="#141414" stroke-width="2.5" fill="none"/></svg>
  <article class="blog-card" style="left:105px"><div class="blog-photo" role="img" aria-label="Polishing a black car bonnet" style="background:linear-gradient(135deg,#1b1b1d,#3a3a3e 50%,#8b1c22)"></div><div class="date">Mar 25,2023</div><h3>Lorem ipsum dolor sit amet, consectetur</h3><a class="btn">Read More</a></article>
  <article class="blog-card" style="left:445px"><div class="blog-photo" role="img" aria-label="Brake disc and caliper being serviced" style="background:linear-gradient(135deg,#2a2b30,#9a9ca2 55%,#d8c23a)"></div><div class="date">Mar 26,2023</div><h3>Lorem ipsum dolor sit amet, consectetur</h3><a class="btn">Read More</a></article>
  <article class="blog-card" style="left:785px"><div class="blog-photo" role="img" aria-label="Mechanic inspecting underside of a raised car" style="background:linear-gradient(135deg,#1e3350,#6f8cab 55%,#2a3f5d)"></div><div class="date">Mar 27,2023</div><h3>Lorem ipsum dolor sit amet, consectetur</h3><a class="btn">Read More</a></article>
</section>

<section class="testimonials">
  <h2 class="section-title" style="top:3618px;left:20px">Testimonials</h2>
  <div class="testi-band"></div>
  <svg class="arrow" style="left:64px;top:3872px" width="10" height="16" viewBox="0 0 10 16"><path d="M8 1 L2 8 L8 15" stroke="#fff" stroke-width="2" fill="none"/></svg>
  <svg class="arrow" style="left:1112px;top:3872px" width="10" height="16" viewBox="0 0 10 16"><path d="M2 1 L8 8 L2 15" stroke="#fff" stroke-width="2" fill="none"/></svg>
  <div class="testi-card" style="left:160px">
    <div class="qm">&ldquo;</div>
    <p>Lorem Ipsum is simply dummy text of the printing and typesetting industry. Lorem Ipsum has been the industry's standard dummy text ever since the 1500s, when an unknown printer took a galley of type and scrambled it to make the printing and typesetting</p>
    <div class="avatar" role="img" aria-label="Client portrait"></div>
    <div class="who-name">Dalton Reyes</div><div class="who-role">Client</div>
  </div>
  <div class="testi-card" style="left:653px">
    <div class="qm">&ldquo;</div>
    <p>Lorem Ipsum is simply dummy text of the printing and typesetting industry. Lorem Ipsum has been the industry's standard dummy text ever since the 1500s, when an unknown printer took a galley of type and scrambled it to make the printing and typesetting</p>
    <div class="avatar" role="img" aria-label="Client portrait"></div>
    <div class="who-name">Owen Pratt</div><div class="who-role">Client</div>
  </div>
</section>

<footer class="footer">
  <div class="foot-brand">Kestrel Auto Repair</div>
  <svg class="abs" style="left:108px;top:132px" width="20" height="20" viewBox="0 0 24 24"><path d="M6.6 10.8a15 15 0 0 0 6.6 6.6l2.2-2.2a1 1 0 0 1 1-.25 11.4 11.4 0 0 0 3.6.57 1 1 0 0 1 1 1V20a1 1 0 0 1-1 1A17 17 0 0 1 3 4a1 1 0 0 1 1-1h3.5a1 1 0 0 1 1 1c0 1.25.2 2.45.57 3.57a1 1 0 0 1-.25 1z" fill="#fff"/></svg>
  <div class="foot-h" style="left:138px;top:133px">Call Us</div>
  <div class="foot-t" style="left:132px;top:170px">+1 555 014 2290</div>
  <svg class="abs" style="left:108px;top:212px" width="18" height="24" viewBox="0 0 18 24"><path d="M9 0a9 9 0 0 0-9 9c0 6.5 9 15 9 15s9-8.5 9-15a9 9 0 0 0-9-9zm0 12.5A3.5 3.5 0 1 1 9 5.5a3.5 3.5 0 0 1 0 7z" fill="#fff"/></svg>
  <div class="foot-h" style="left:138px;top:216px">Our Location</div>
  <div class="foot-t" style="left:140px;top:252px;width:240px">Lorem Ipsum Lorem Ipsum is simply dummy text of the</div>
  <div class="foot-h" style="left:474px;top:133px">Working Hours</div>
  <div class="foot-t" style="left:476px;top:170px">Mon - Fri &nbsp;&nbsp; 8.00 Am to 9.00Pm</div>
  <div class="foot-t" style="left:476px;top:195px">Sat &amp; Sun &nbsp; 9.00 Am to 6.00Pm</div>
  <div class="foot-h" style="left:820px;top:133px">Click Here for&nbsp; Quotes</div>
  <a class="btn foot-btn">Get Quote</a>
  <div class="foot-line"></div>
  <div class="copyright">2023 © Kestrel Auto Repair | All Rights Reserved</div>
</footer>

</body>
</html>
```